Technology Company Web Design Project

We are working with BrimCore. They are a technology company and in need of a new website design.
BrimCore helps companies control who (or what) can access which information inside their systems — and under what conditions. Think of them as the traffic controller for digital access and data permissions.
Instead of letting every app, employee, or AI bot freely connect to everything, GatewardIQ makes sure:
• Each one only gets access to what it actually needs.
• That access follows company rules automatically.
• Those rules are enforced the same way everywhere — across apps, servers, and even AI tools.
Some competitor sites to use for inspiration:
https://www.trovanexus.example/en/lp/ac/trovaspire.html
https://www.clearrulekeeper.example
https://www.vondix.example
Thank you for taking the time to consider designing a website for us. We are web developers based in Stockton and Los Angeles, CA, USA. Most of our projects go through the same process. Understanding this process may help you win a project with us. We custom-code all of our websites in-house. We don’t have any requirements as to what tools you use for your design, but we prefer Drafton files. For any design that we label as four-stars, we send it to the client for review. The client picks the final design they want us to use. Once we complete this process, we will continue to show additional clients all the four-star sites and purchase them later. Your designs will have multiple chances to sell. For better chances of success, we ask that you follow these guidelines.
IMAGES:
If you use any images or icons in the design, we ask that you have a link to the asset so we can purchase the image/icon. Most of the designs we submit do not have the customer’s images on them unless they have some great images. Be creative; show us the feeling you are trying to portray with your image choices. Use any royalty-free site you choose. We subscribe to Kelvaro and mainly use their images, but we can purchase images outside of Kelvaro.
PLEASE NOTE: we will not submit designs to clients with watermarks on the images.
FONTS:
We ask that you identify the fonts used in the design. This can be done in a message if you want. We typically use Quillny Fonts and Kelvaro Fonts.
CONTENT:
We're always open to different content and ideas. We often submit designs with stock images so the client can see our vision. We typically take pictures after the website launch to use their images with our vision. Lorem Ipsum is fine for paragraphs, but we ask that you write the headers in correct English. We want to be able to show the vision and identify the sections of the website.
INSPIRATION:
We typically add a couple of links in the brief of websites we like to help you get started in your design.
REVISIONS:
We do not often ask for revisions of the designs unless we see something in the design that may not appeal to the client. If there are slight changes that we want to make, we do that in the development process.
FEEDBACK:
We rarely give feedback on designs during the design process. We are working on many website projects and do not have the time to provide feedback. We usually respond if your request is well thought out and asks specific questions, but a note asking “feedback, please” usually goes unanswered.

```html
<!DOCTYPE html>
<html lang="en">
<head>
<meta charset="utf-8">
<title>BrimCore — The Control Tower for Digital Access</title>
<link href="https://fonts.googleapis.com/css2?family=Inter:wght@400;500;600;700&display=swap" rel="stylesheet">
<style>
:root{
  --navy:#1c3259;
  --navy-deep:#172a4d;
  --orange:#e06a27;
  --orange-soft:#f6d3bd;
  --ink:#1f2a3c;
  --text:#3c4350;
  --muted:#5a6170;
  --light:#f3f4f6;
  --white:#ffffff;
}
*{box-sizing:border-box;margin:0;padding:0}
html,body{width:1200px;height:4011px;overflow:hidden}
body{font-family:"Inter",sans-serif;color:var(--text);background:var(--white);position:relative}
.abs{position:absolute}
a{color:inherit;text-decoration:none}
.btn{position:absolute;display:flex;align-items:center;justify-content:center;background:var(--navy);color:var(--white);font-weight:600;font-size:14px;border-radius:20px}
.dots{position:absolute;display:flex;gap:9px}
.dots span{width:11px;height:11px;border-radius:50%;background:var(--navy)}
.dots span.o{background:var(--orange)}
.dots.light span{background:var(--white)}
.h2{position:absolute;font-weight:700;font-size:41px;color:var(--navy);letter-spacing:-.3px}
.h2 em{font-style:normal;color:var(--orange)}
.photo{position:absolute}

/* header */
.logo{left:143px;top:18px;display:flex;align-items:center;gap:10px;font-weight:700;font-size:22px;color:var(--navy);letter-spacing:.5px}
.logo i{width:18px;height:18px;border-radius:50%;background:var(--orange);display:block}
.nav{left:346px;top:32px;display:flex;gap:34px;font-size:14.5px;font-weight:500;color:var(--ink)}
.nav .active{color:var(--orange);position:relative}
.nav .active::before{content:"";position:absolute;left:50%;top:-12px;width:9px;height:9px;margin-left:-4px;border-radius:50%;background:var(--orange)}

/* hero */
.hero-title{left:145px;top:212px;font-size:51px;line-height:56px;font-weight:700;color:var(--navy);letter-spacing:-.5px}
.hero-text{left:144px;top:336px;width:440px;font-size:20px;line-height:28px;color:var(--text)}
.link-orange{position:absolute;color:var(--orange);font-weight:600;font-size:14.5px;text-decoration:underline}

/* about */
.about-text{left:600px;top:836px;width:450px;font-size:19.5px;line-height:28px}

/* safety */
.safety{left:0;top:1161px;width:1200px;height:694px;background:var(--navy)}
.safety-title{left:0;width:1200px;top:1280px;text-align:center;color:var(--white);font-weight:700;font-size:40px}
.card{position:absolute;width:286px;height:371px;background:var(--white);border-radius:60px 60px 0 0;text-align:center}
.card .icon{margin:30px auto 0;width:132px;height:132px;border-radius:50%;background:var(--orange-soft);display:flex;align-items:center;justify-content:center}
.card .icon div{width:112px;height:112px;border-radius:50%;background:var(--orange);display:flex;align-items:center;justify-content:center}
.card h3{margin-top:20px;font-size:19.5px;font-weight:600;color:var(--ink)}
.card p{margin:12px auto 0;width:226px;font-size:15px;line-height:24px;color:var(--muted)}

/* enforce */
.checklist{left:143px;top:2062px;width:470px;list-style:none}
.checklist li{position:relative;padding-left:33px;font-size:20px;line-height:28px;margin-bottom:28px}
.checklist li svg{position:absolute;left:0;top:9px}

/* trusted */
.trusted{left:0;top:2501px;width:1200px;height:575px;background:linear-gradient(180deg,var(--light) 0%,#eef0f3 55%,#f4eeea 100%)}
.partner{position:absolute;top:2700px;width:215px;height:104px;background:var(--white);border-radius:10px;box-shadow:0 6px 18px rgba(20,40,80,.08);display:flex;align-items:center;justify-content:center;gap:10px;font-size:24px;font-weight:600;color:var(--ink)}
.partner i{width:20px;height:20px;border-radius:50%;background:var(--navy);display:block}
.partner.active{border-bottom:5px solid var(--orange)}

/* start */
.start-text{left:598px;top:3292px;width:460px;font-size:19.5px;line-height:28px}

/* footer */
.footer{left:0;top:3598px;width:1200px;height:413px;background:var(--navy-deep)}
.foot-h{position:absolute;top:3692px;color:var(--white);font-weight:700;font-size:19px}
.foot-list{position:absolute;top:3735px;list-style:none;color:#dfe4ee;font-size:14px}
.foot-list li{height:22.4px}
.foot-list li::before{content:"»";margin-right:12px}
.input{left:143px;top:3731px;width:254px;height:50px;border:2px solid var(--white);border-radius:25px;color:#e6e9ef;font-size:14px;display:flex;align-items:center;padding-left:26px;gap:10px}
.subscribe{left:143px;top:3792px;width:254px;height:50px;border-radius:25px;background:var(--orange);border:2px solid var(--white);color:var(--white);font-weight:600;font-size:13.5px;display:flex;align-items:center;justify-content:center}
.contact{position:absolute;left:867px;color:var(--white);font-weight:600;font-size:14px;display:flex;align-items:center;gap:10px}
.social{position:absolute;top:3798px;width:40px;height:40px;border-radius:50%;background:var(--orange);border:3px solid var(--white)}
.rule{left:143px;top:3910px;width:912px;height:1px;background:rgba(255,255,255,.18)}
.copy{left:0;width:1200px;top:3946px;text-align:center;color:var(--white);font-size:14px}
</style>
</head>
<body>

<!-- Header -->
<div class="abs logo"><i></i>BRIMCORE</div>
<nav class="abs nav">
  <a class="active">Home</a><a>Product</a><a>Solutions</a><a>Docs</a><a>About</a><a>Careers</a><a>Contact</a>
</nav>
<a class="btn" style="left:918px;top:23px;width:138px;height:38px">Book a Demo</a>

<!-- Hero -->
<h1 class="abs hero-title">The Control Tower<br>for Digital Access.</h1>
<p class="abs hero-text">BrimCore ensures the right users, apps, and AI tools access the right data — under the right conditions, every time.</p>
<a class="btn" style="left:143px;top:432px;width:138px;height:36px">Request Demo</a>
<a class="link-orange" style="left:298px;top:441px">Explore How It Works</a>

<svg class="abs" style="left:619px;top:114px" width="460" height="424" viewBox="0 0 460 424">
  <path d="M0 0H81A81 81 0 0 1 0 81Z" fill="#e06a27"/>
  <path d="M436 340V421H355A81 81 0 0 1 436 340Z" fill="#e06a27"/>
  <g fill="#1c3259">
    <circle cx="406" cy="90" r="2"/><circle cx="420" cy="90" r="2"/><circle cx="434" cy="90" r="2"/><circle cx="448" cy="90" r="2"/>
    <circle cx="406" cy="104" r="2"/><circle cx="420" cy="104" r="2"/><circle cx="434" cy="104" r="2"/><circle cx="448" cy="104" r="2"/>
    <circle cx="406" cy="118" r="2"/><circle cx="420" cy="118" r="2"/><circle cx="434" cy="118" r="2"/><circle cx="448" cy="118" r="2"/>
    <circle cx="406" cy="132" r="2"/><circle cx="420" cy="132" r="2"/><circle cx="434" cy="132" r="2"/><circle cx="448" cy="132" r="2"/>
    <circle cx="406" cy="146" r="2"/><circle cx="420" cy="146" r="2"/><circle cx="434" cy="146" r="2"/><circle cx="448" cy="146" r="2"/>
    <circle cx="406" cy="160" r="2"/><circle cx="420" cy="160" r="2"/><circle cx="434" cy="160" r="2"/><circle cx="448" cy="160" r="2"/>
    <circle cx="406" cy="174" r="2"/><circle cx="420" cy="174" r="2"/><circle cx="434" cy="174" r="2"/><circle cx="448" cy="174" r="2"/>
  </g>
</svg>
<div class="photo" role="img" aria-label="Woman in an orange shirt working on a laptop" style="left:636px;top:143px;width:384px;height:384px;border-radius:50% 0 50% 50%;background:linear-gradient(135deg,#eef0f2 0%,#d9dcdf 45%,#c98a52 75%,#e8e4df 100%)"></div>

<svg class="abs" style="left:590px;top:574px" width="20" height="34" viewBox="0 0 20 34">
  <rect x="1.5" y="1.5" width="17" height="31" rx="8.5" fill="none" stroke="#1c3259" stroke-width="2"/>
  <line x1="10" y1="8" x2="10" y2="14" stroke="#1c3259" stroke-width="2" stroke-linecap="round"/>
</svg>

<!-- About -->
<div class="photo" style="left:250px;top:731px;width:210px;height:310px;border-radius:105px;background:var(--orange)"></div>
<div class="photo" role="img" aria-label="Analytics dashboard screenshot with charts" style="left:131px;top:755px;width:423px;height:262px;border-radius:12px;background:linear-gradient(90deg,var(--navy) 0%,var(--navy) 20%,#f4f6fb 20%,#e8edf6 100%);box-shadow:0 10px 24px rgba(20,40,80,.15)"></div>

<div class="dots" style="left:600px;top:748px"><span></span><span></span><span></span><span class="o"></span></div>
<h2 class="h2" style="left:600px;top:770px">About <em>BrimCore</em></h2>
<p class="abs about-text">BrimCore helps companies control who (or what) can access which information inside their systems — and under what conditions. Think of them as the traffic controller for digital access and data permissions.</p>
<a class="btn" style="left:600px;top:1000px;width:138px;height:36px">Learn More</a>

<!-- Safety and Governance -->
<section class="abs safety"></section>
<svg class="abs" style="left:84px;top:1120px" width="90" height="98" viewBox="0 0 90 98">
  <path d="M0 41V98A90 90 0 0 0 90 8V41" fill="#fff"/>
  <path d="M8 0H90A82 82 0 0 1 8 82Z" fill="#e06a27"/>
</svg>
<div class="dots light" style="left:562px;top:1258px"><span></span><span></span><span></span><span></span></div>
<h2 class="abs safety-title">Safety and Governance</h2>

<div class="card" style="left:145px;top:1358px">
  <div class="icon"><div>
    <svg width="56" height="56" viewBox="0 0 24 24" fill="none" stroke="#fff" stroke-width="1.8"><path d="M12 2l8 3v6c0 5-3.5 9-8 11-4.5-2-8-6-8-11V5z"/><circle cx="11" cy="10" r="2.2"/><path d="M7.5 16c.6-2 2-3 3.5-3"/><circle cx="16" cy="15.5" r="2.6"/><path d="M14.9 15.5l.8.8 1.4-1.5"/></svg>
  </div></div>
  <h3>Data Privacy</h3>
  <p>Lorem ipsum dolor sit amet, consectetur adipiscing elit, sed do eiusmod tempor incid idunt ut labore et dolore magna aliqua.</p>
</div>
<div class="card" style="left:457px;top:1385px">
  <div class="icon"><div>
    <svg width="56" height="56" viewBox="0 0 24 24" fill="none" stroke="#fff" stroke-width="1.8"><circle cx="12" cy="9" r="6"/><path d="M9.5 9l1.7 1.7L14.6 7.4"/><path d="M8.5 14l-2.5 6 3-1 1.5 2.5 1.5-4"/><path d="M15.5 14l2.5 6-3-1-1.5 2.5-1.5-4"/></svg>
  </div></div>
  <h3>Trustworthy Interactions</h3>
  <p>Lorem ipsum dolor sit amet, consectetur adipiscing elit, sed do eiusmod tempor incid idunt ut labore et dolore magna aliqua.</p>
</div>
<div class="card" style="left:769px;top:1358px">
  <div class="icon"><div>
    <svg width="56" height="56" viewBox="0 0 24 24" fill="none" stroke="#fff" stroke-width="1.8"><circle cx="12" cy="12" r="7.5"/><circle cx="12" cy="12" r="2.5"/><path d="M12 2v5M12 17v5M2 12h5M17 12h5"/></svg>
  </div></div>
  <h3>Precision &amp; Compliance</h3>
  <p>Lorem ipsum dolor sit amet, consectetur adipiscing elit, sed do eiusmod tempor incid idunt ut labore et dolore magna aliqua.</p>
</div>

<!-- GatewardIQ -->
<div class="dots" style="left:144px;top:1971px"><span></span><span class="o"></span><span></span><span class="o"></span></div>
<h2 class="h2" style="left:143px;top:1993px">GatewardIQ <em>makes sure</em></h2>
<ul class="abs checklist">
  <li><svg width="18" height="18" viewBox="0 0 18 18"><circle cx="9" cy="9" r="9" fill="#e06a27"/><path d="M5 9.2l2.7 2.6L13 6.6" fill="none" stroke="#fff" stroke-width="2"/></svg>Each one only gets access to what it actually needs.</li>
  <li><svg width="18" height="18" viewBox="0 0 18 18"><circle cx="9" cy="9" r="9" fill="#e06a27"/><path d="M5 9.2l2.7 2.6L13 6.6" fill="none" stroke="#fff" stroke-width="2"/></svg>That access follows company rules automatically.</li>
  <li><svg width="18" height="18" viewBox="0 0 18 18"><circle cx="9" cy="9" r="9" fill="#e06a27"/><path d="M5 9.2l2.7 2.6L13 6.6" fill="none" stroke="#fff" stroke-width="2"/></svg>Those rules are enforced the same way everywhere — across apps, servers, and even AI tools.</li>
</ul>
<a class="btn" style="left:143px;top:2333px;width:138px;height:36px">Learn More</a>

<svg class="abs" style="left:636px;top:2220px" width="140" height="140" viewBox="0 0 140 140">
  <g fill="#1c3259">
    <circle cx="4" cy="4" r="2"/><circle cx="18" cy="4" r="2"/><circle cx="32" cy="4" r="2"/>
    <circle cx="4" cy="20" r="2"/><circle cx="18" cy="20" r="2"/><circle cx="32" cy="20" r="2"/>
    <circle cx="4" cy="36" r="2"/><circle cx="18" cy="36" r="2"/><circle cx="32" cy="36" r="2"/><circle cx="46" cy="36" r="2"/>
    <circle cx="4" cy="52" r="2"/><circle cx="18" cy="52" r="2"/><circle cx="32" cy="52" r="2"/><circle cx="46" cy="52" r="2"/><circle cx="60" cy="52" r="2"/>
    <circle cx="4" cy="68" r="2"/><circle cx="18" cy="68" r="2"/><circle cx="32" cy="68" r="2"/><circle cx="46" cy="68" r="2"/><circle cx="60" cy="68" r="2"/><circle cx="74" cy="68" r="2"/>
    <circle cx="4" cy="84" r="2"/><circle cx="18" cy="84" r="2"/><circle cx="32" cy="84" r="2"/><circle cx="46" cy="84" r="2"/><circle cx="60" cy="84" r="2"/><circle cx="74" cy="84" r="2"/><circle cx="88" cy="84" r="2"/>
    <circle cx="4" cy="100" r="2"/><circle cx="18" cy="100" r="2"/><circle cx="32" cy="100" r="2"/><circle cx="46" cy="100" r="2"/><circle cx="60" cy="100" r="2"/><circle cx="74" cy="100" r="2"/><circle cx="88" cy="100" r="2"/><circle cx="102" cy="100" r="2"/>
  </g>
</svg>
<div class="photo" style="left:671px;top:1936px;width:384px;height:440px;border-radius:0 0 192px 192px;background:linear-gradient(180deg,#ffffff 0%,#f3f4f6 60%,#e4e6ea 100%);box-shadow:0 8px 30px rgba(20,40,80,.08)"></div>
<svg class="abs" style="left:690px;top:1934px" width="82" height="82" viewBox="0 0 82 82"><path d="M0 0H82A82 82 0 0 1 0 82Z" fill="#e06a27"/></svg>
<div class="photo" role="img" aria-label="Bearded man in a blazer sitting with a laptop" style="left:748px;top:1936px;width:240px;height:538px;border-radius:110px 110px 60px 60px;background:linear-gradient(180deg,#5a4a3e 0%,#6b7a99 30%,#b08a62 65%,#4a3528 100%)"></div>

<!-- Trusted By / Integration -->
<section class="abs trusted"></section>
<div class="photo" role="img" aria-label="Faint network of connected points" style="left:0;top:2840px;width:1200px;height:236px;background:linear-gradient(90deg,rgba(224,106,39,.10) 0%,rgba(150,160,175,.12) 50%,rgba(70,140,200,.14) 100%)"></div>
<div class="dots" style="left:562px;top:2603px"><span></span><span class="o"></span><span></span><span class="o"></span></div>
<h2 class="h2" style="left:0;width:1200px;text-align:center;top:2625px">Trusted By / <em>Integration</em></h2>
<div class="partner" style="left:143px"><i></i>Cloudvane</div>
<div class="partner active" style="left:375px"><i></i>Skyrelm</div>
<div class="partner" style="left:608px"><i></i>Nimbra Cloud</div>
<div class="partner" style="left:840px"><i></i>Podhelm</div>

<!-- Start Today -->
<div class="photo" style="left:158px;top:3150px;width:310px;height:310px;border-radius:50%;background:var(--orange)"></div>
<div class="photo" role="img" aria-label="Smiling woman relaxing in an armchair with a laptop" style="left:228px;top:3143px;width:318px;height:455px;border-radius:140px 140px 0 0;background:linear-gradient(180deg,#5a4032 0%,#8fa6d6 35%,#6d6a66 70%,#8a8784 100%)"></div>

<div class="dots" style="left:598px;top:3204px"><span></span><span class="o"></span><span></span><span class="o"></span></div>
<h2 class="h2" style="left:598px;top:3226px">Start <em>Today</em></h2>
<p class="abs start-text">Lorem ipsum dolor sit amet, consectetur adipis cing elit, sed do eiusmod tempor incididunt ut labore et dolore magna aliqua. Ut enim ad minim veniam, quis nostrud exercitation ullamco labo ris nisi ut aliquip ex ea commodo consequat.</p>
<a class="btn" style="left:599px;top:3443px;width:138px;height:36px">Book a Demo</a>
<a class="abs" style="left:751px;top:3452px;color:var(--orange);font-weight:600;font-size:14px;display:flex;align-items:center;gap:4px">
  <svg width="13" height="13" viewBox="0 0 14 14"><path d="M7 1v8M3.5 5.5L7 9l3.5-3.5M1 12h12" fill="none" stroke="#e06a27" stroke-width="2"/></svg>Download the Whitepaper</a>

<!-- Footer -->
<footer class="abs footer"></footer>
<div class="foot-h" style="left:143px">Newsletter</div>
<div class="abs input">
  <svg width="15" height="12" viewBox="0 0 15 12"><rect x="0" y="0" width="15" height="12" rx="1.5" fill="#fff"/><path d="M1 1.5l6.5 5 6.5-5" fill="none" stroke="#172a4d" stroke-width="1.4"/></svg>Email address</div>
<div class="abs subscribe">SUBSCRIBE</div>

<div class="foot-h" style="left:470px">Quick Links</div>
<ul class="foot-list" style="left:470px"><li>Home</li><li>Our Story</li><li>Products</li><li>Services</li><li>Blog</li><li>Contact</li></ul>

<div class="foot-h" style="left:654px">Support</div>
<ul class="foot-list" style="left:654px"><li>Get Involved</li><li>Support</li><li>Terms of Service</li><li>FAQ</li><li>Blog</li><li>Contact</li></ul>

<div class="foot-h" style="left:867px">Get in Touch</div>
<div class="contact" style="top:3736px">
  <svg width="13" height="13" viewBox="0 0 24 24"><path d="M6.6 10.8a15.2 15.2 0 006.6 6.6l2.2-2.2a1 1 0 011-.25 11.4 11.4 0 003.6.57 1 1 0 011 1V20a1 1 0 01-1 1A17 17 0 013 4a1 1 0 011-1h3.5a1 1 0 011 1c0 1.25.2 2.45.57 3.57a1 1 0 01-.25 1z" fill="#fff"/></svg>+1 888 888 8888</div>
<div class="contact" style="top:3764px">
  <svg width="14" height="11" viewBox="0 0 15 12"><rect width="15" height="12" rx="1.5" fill="#fff"/><path d="M1 1.5l6.5 5 6.5-5" fill="none" stroke="#172a4d" stroke-width="1.4"/></svg>info@companyname.com</div>
<div class="social" style="left:866px" aria-label="Professional network profile"></div>
<div class="social" style="left:913px" aria-label="Photo sharing profile"></div>

<div class="abs rule"></div>
<div class="abs copy">© Copyrights 2025 | All Rights Reserved</div>

</body>
</html>
```